全国の1人〜2人で営業されている理・美容室のオーナーさん方にコロナでも全く影響を受けてない当サロンのノウハウを読んで頂きたいと思っています。
これからのサロンのあり方、考え方、今すぐに取り入れるべき技術や商品、売り上げの上げ方などをお伝えします。本気で環境を変えたい方、美容師の仕事、接客、人をキレイにすることが大好きな方、意識の高いお客様に囲まれずっと通って頂けるような、そんな美容室を一緒に作って行きたいです。

この度はご提案、修正と本当にありがとうございました。最後の最後までかなり悩みました。
初めての電子書籍で良い表紙デザインと出会うことが出来ました。

今回、ご提案頂いた皆さん、本当にありがとうございました。初心者の自分に親身になって頂き、皆さんの丁寧なデザインに感動しました。また2冊目も考えています。ご縁があればまたよろしくお願いします。

```html
<!DOCTYPE html>
<html lang="ja">
<head>
<meta charset="UTF-8">
<title>これからサロンが生き残る方法</title>
<link href="https://fonts.googleapis.com/css2?family=Noto+Sans+JP:wght@500;700;900&family=Kosugi+Maru&display=swap" rel="stylesheet">
<style>
  :root {
    --paper: #ffffff;
    --maroon: #7a1826;
    --ink: #111111;
    --bubble: #5fe03c;
    --frame: #3a2a2a;
    --scene-light: #f6f1ea;
    --scene-mid: #e6dccd;
  }
  html, body {
    margin: 0;
    padding: 0;
    width: 750px;
    height: 1200px;
    overflow: hidden;
    background: var(--paper);
  }
  .cover {
    position: relative;
    width: 750px;
    height: 1200px;
    background: var(--paper);
    font-family: "Noto Sans JP", sans-serif;
    color: var(--ink);
  }
  .audience-band {
    position: absolute;
    left: 25px;
    top: 20px;
    width: 700px;
    height: 62px;
    background: var(--maroon);
    color: #fff;
    font-weight: 500;
    font-size: 31px;
    line-height: 62px;
    text-align: center;
    letter-spacing: 1px;
  }
  .hope-bubble {
    position: absolute;
    left: 178px;
    top: 108px;
    width: 340px;
    height: 118px;
    background: var(--bubble);
    border-radius: 50%;
    font-family: "Kosugi Maru", sans-serif;
    font-size: 32px;
    line-height: 42px;
    text-align: center;
    padding-top: 17px;
    box-sizing: border-box;
  }
  .side-note {
    position: absolute;
    left: 30px;
    top: 112px;
    width: 86px;
    height: 880px;
    border: 3px solid var(--frame);
    box-sizing: border-box;
    writing-mode: vertical-rl;
    color: var(--maroon);
    font-weight: 700;
    font-size: 31px;
    line-height: 80px;
    letter-spacing: 1px;
    text-align: center;
  }
  .headline {
    position: absolute;
    left: 205px;
    top: 244px;
    width: 530px;
    margin: 0;
    font-weight: 900;
    font-size: 39px;
    line-height: 60px;
    white-space: nowrap;
    transform: rotate(2deg);
    transform-origin: left center;
  }
  .salon-scene {
    position: absolute;
    left: 238px;
    top: 318px;
    width: 440px;
    height: 490px;
    background: radial-gradient(ellipse at 50% 55%, var(--scene-mid), var(--scene-light) 70%, var(--paper));
  }
  .title {
    position: absolute;
    left: 200px;
    top: 830px;
    width: 520px;
    margin: 0;
    font-weight: 900;
    font-size: 60px;
    line-height: 78px;
    text-align: center;
    letter-spacing: 1px;
  }
  .author {
    position: absolute;
    left: 200px;
    top: 1028px;
    width: 520px;
    font-weight: 700;
    font-size: 42px;
    text-align: center;
    letter-spacing: 2px;
  }
</style>
</head>
<body>
  <main class="cover">
    <div class="audience-band">全国の理美容室のサロンのオーナー様へ</div>
    <div class="hope-bubble">どんな逆境にも<br>チャンスは必ずある！</div>
    <div class="side-note">コロナでも全く影響を受けていない当サロンのノウハウを！</div>
    <p class="headline">コロナや景気に左右されない</p>
    <div class="salon-scene" role="img" aria-label="ペンダントライトの下、鏡の前で美容師がお客様の髪を仕上げる線画のサロン風景と観葉植物"></div>
    <h1 class="title">これからサロンが<br>生き残る方法</h1>
    <div class="author">著者　さくらいはると</div>
  </main>
</body>
</html>
```